Manufacturing company needs new business card.

I need a unique Business Card that will truly stand out. Nothing too busy. Simple is good, right? Not looking for a standard design either. No cookie cutter layout. I am just looking for something interesting and a bit different. Does't have to completely off the wall crazy, just not your run of the mill business card. Clean and modern with a touch of industrial.

Target Market(s)

Air conditioning industry, Architects, builders.

Industry/Entity Type

Business

Contact Information for Business Card

Details to be included on card are:

Peter Vance
Managing Director

T: 1300 847 519
M: 0428 593 174
W: www.brenvaleworks.com.au
E: peter.vance@brenvaleworks.com.au
A: 58 Harwick Lane, Sydney NSW 2000

Font styles to use
Sans Serif

Colors
0355a3
848484
fbfbfb

Requirements
Must have
• Card design must be landscape.

```html
<!DOCTYPE html>
<html lang="en">
<head>
<meta charset="utf-8">
<title>Brenvale Works – Business Card</title>
<link rel="stylesheet" href="https://fonts.googleapis.com/css2?family=Arimo:wght@400;700&display=swap">
<style>
  :root {
    --brand-blue: #0355a3;
    --band-blue: #1e4fa6;
    --steel-grey: #848484;
    --card-white: #fbfbfb;
    --backdrop: #2a2a2a;
    --ink-white: #ffffff;
  }
  * { margin: 0; padding: 0; box-sizing: border-box; }
  html, body { width: 1200px; height: 997px; overflow: hidden; }
  body {
    background: var(--backdrop);
    font-family: "Arimo", Arial, sans-serif;
    position: relative;
  }

  .card {
    position: absolute;
    width: 560px; height: 340px;
    border-radius: 3px;
    box-shadow: 0 18px 40px rgba(0,0,0,.6);
    overflow: hidden;
  }

  /* Shared wordmark */
  .wordmark-group { display: flex; align-items: center; gap: 14px; }
  .wordmark-square { flex: none; }
  .wordmark-text { display: flex; flex-direction: column; align-items: flex-end; }
  .wordmark { font-weight: 700; letter-spacing: .2px; line-height: 1; white-space: nowrap; }
  .tagline {
    font-size: 10px; letter-spacing: 6px; margin-top: 4px; padding-top: 4px;
    border-top: 1px solid; width: 100%; text-align: right;
  }

  /* Reverse side */
  .card-back {
    left: 80px; top: 140px;
    background: linear-gradient(160deg, #2a62c0, var(--band-blue) 60%, #17449a);
    display: flex; align-items: center; justify-content: center;
  }
  .card-back .wordmark-square { width: 28px; height: 28px; background: var(--ink-white); }
  .card-back .wordmark { color: var(--ink-white); font-size: 28px; }
  .card-back .tagline { color: rgba(255,255,255,.85); border-top-color: rgba(255,255,255,.7); }

  /* Information side */
  .card-front {
    left: 560px; top: 470px;
    background: var(--card-white);
    display: flex; flex-direction: column;
  }
  .front-identity {
    height: 130px;
    display: flex; align-items: center; justify-content: space-between;
    padding: 0 34px;
  }
  .front-identity .wordmark-square { width: 48px; height: 48px; background: var(--brand-blue); }
  .front-identity .wordmark { color: var(--brand-blue); font-size: 24px; }
  .front-identity .tagline { color: var(--steel-grey); border-top-color: var(--steel-grey); font-size: 9px; letter-spacing: 5px; }
  .person { text-align: right; }
  .person-name { color: var(--brand-blue); font-size: 22px; font-weight: 700; letter-spacing: .5px; white-space: nowrap; }
  .person-title { color: var(--steel-grey); font-size: 12px; margin-top: 3px; letter-spacing: .3px; }

  .rule { height: 6px; background: var(--steel-grey); flex: none; }
  .rule-gap { height: 5px; background: var(--card-white); flex: none; }

  .contact-band {
    height: 138px;
    background: var(--band-blue);
    color: var(--ink-white);
    display: flex; flex-direction: column; align-items: center; justify-content: center;
    gap: 12px;
    font-size: 15px; font-weight: 700; line-height: 1.6;
  }
  .contact-icons { display: flex; gap: 16px; }
  .contact-icon {
    width: 22px; height: 22px; border-radius: 50%;
    background: var(--card-white);
    display: flex; align-items: center; justify-content: center;
  }
  .contact-icon svg { width: 13px; height: 13px; }
  .contact-columns { display: flex; gap: 40px; white-space: nowrap; }
  .contact-column.phones { text-align: right; }

  .website-strip {
    flex: 1;
    display: flex; align-items: center; justify-content: center;
    color: var(--brand-blue); font-size: 20px; font-weight: 700;
  }
</style>
</head>
<body>

  <section class="card card-back" aria-label="Business card reverse">
    <div class="wordmark-group">
      <span class="wordmark-square"></span>
      <div class="wordmark-text">
        <span class="wordmark">Brenvale Works</span>
        <span class="tagline">AUSTRALIA</span>
      </div>
    </div>
  </section>

  <section class="card card-front" aria-label="Business card front">
    <div class="front-identity">
      <div class="wordmark-group">
        <span class="wordmark-square"></span>
        <div class="wordmark-text">
          <span class="wordmark">Brenvale Works</span>
          <span class="tagline">AUSTRALIA</span>
        </div>
      </div>
      <div class="person">
        <div class="person-name">PETER VANCE</div>
        <div class="person-title">MANAGING DIRECTOR</div>
      </div>
    </div>

    <div class="rule"></div>
    <div class="rule-gap"></div>

    <div class="contact-band">
      <div class="contact-icons">
        <span class="contact-icon" aria-label="Phone">
          <svg viewBox="0 0 14 14"><path fill="#1e4fa6" d="M2 4c0-1 1-2 5-2s5 1 5 2v1H9.5V4h-5v1H2z M4 6h6l1.5 5h-9z"/></svg>
        </span>
        <span class="contact-icon" aria-label="Email">
          <svg viewBox="0 0 14 14"><rect x="1.5" y="3.5" width="11" height="7" fill="none" stroke="#1e4fa6" stroke-width="1.3"/><path d="M1.5 3.5 7 8l5.5-4.5" fill="none" stroke="#1e4fa6" stroke-width="1.3"/></svg>
        </span>
        <span class="contact-icon" aria-label="Website">
          <svg viewBox="0 0 14 14"><circle cx="7" cy="7" r="5.3" fill="none" stroke="#1e4fa6" stroke-width="1.2"/><ellipse cx="7" cy="7" rx="2.3" ry="5.3" fill="none" stroke="#1e4fa6" stroke-width="1"/><path d="M1.7 7h10.6" stroke="#1e4fa6" stroke-width="1"/></svg>
        </span>
      </div>
      <div class="contact-columns">
        <div class="contact-column phones">
          <div>1300 847 519</div>
          <div>0428 593 174</div>
        </div>
        <div class="contact-column details">
          <div>peter.vance@brenvaleworks.com.au</div>
          <div>58 Harwick Lane, Sydney NSW 2000</div>
        </div>
      </div>
    </div>

    <div class="rule-gap"></div>
    <div class="rule"></div>

    <div class="website-strip">www.brenvaleworks.com.au</div>
  </section>

</body>
</html>
```